Event Flyer - LGBT Camping Event

I have attached a poster I made (SampleFlyer.pdf) that has all the elements I want. Just don't like the layout and how things look. You can use any colors that make the poster work. I would like to incorporate the Campfest logo into the flyer (uploaded). You are welcome to grab elements from the event website to incorporate into your design (www.campfestmeadowlark.org). I included a couple of pictures to possibly use too. Please include all 8 sponsors and the two hosts are the logos on the bottom of sample flyer - Prairie Alliance & Pinecrest Trail Council. The flyer size needs to be 12"Wide x 17" Tall. Here is a dropbox link to a possible image to use. https://lnk.example/7qTzKwd

Please use the wording;

DON’T MISS this LGBT camping event!

Plan the highlight of your summer TODAY.

It’s almost time for the Rocky Mountain Region’s largest LGBT pride camping event: Campfest Meadowlark!
Join us August 8th-12th for 5 days of fun in a friendly, safe, LGBT affirming environment for everyone, from everywhere!

More Info or Register Online www.sagebrightfest.org

Target Market(s)

LGBT Campers

Industry/Entity Type

Event

Colors

Designer to choose colors to be used in the design.

Requirements
Must have
• Must have text outlined in project description, Campfest logo, sponsor logos and host logos.

```html
<!DOCTYPE html>
<html lang="en">
<head>
<meta charset="utf-8">
<title>Campfest Meadowlark – LGBT Camping Event Flyer</title>
<link rel="stylesheet" href="https://fonts.googleapis.com/css2?family=League+Gothic&family=Open+Sans:wght@400;600;700&display=swap">
<style>
  :root {
    --page-bg: #e9e6e1;
    --forest: #3f7a3c;
    --forest-dark: #2f5f2e;
    --sun-orange: #f7941d;
    --ember: #d9472b;
    --glow: #f4e04d;
    --cream: #fffdf6;
    --bark: #3a2410;
    --ink: #1c1c1c;
    --navy: #24376b;
    --white: #ffffff;
  }
  * { box-sizing: border-box; margin: 0; padding: 0; }
  html, body { width: 1200px; height: 1200px; overflow: hidden; }
  body { background: var(--page-bg); font-family: "Open Sans", Arial, sans-serif; }

  .flyer {
    position: absolute; left: 195px; top: 30px;
    width: 810px; height: 1141px; overflow: hidden;
    background:
      linear-gradient(to bottom, rgba(255,253,246,0) 0, rgba(255,253,246,0) 820px, var(--cream) 970px, var(--cream) 100%),
      radial-gradient(ellipse 380px 250px at 50% 660px, var(--glow) 0%, var(--sun-orange) 45%, rgba(217,71,43,0.9) 80%, rgba(63,122,60,0) 100%),
      var(--forest);
  }

  .hero-photo {
    position: absolute; left: 0; top: 0; width: 810px; height: 610px;
    background:
      radial-gradient(ellipse 380px 240px at 48% 380px, #b98a6a 0%, #8a6f5c 40%, #5a7694 70%, rgba(63,122,60,0.2) 100%),
      linear-gradient(to bottom, #6f6a55 0%, #8a7a5c 50%, rgba(63,122,60,0.6) 100%);
    -webkit-mask-image: linear-gradient(to bottom, #000 70%, transparent 100%);
            mask-image: linear-gradient(to bottom, #000 70%, transparent 100%);
  }

  .hosts { position: absolute; left: 44px; top: 46px; display: flex; flex-direction: column; gap: 10px; }
  .host-name { font-weight: 700; font-size: 17px; color: var(--white); letter-spacing: 0.3px; }

  .intro {
    position: absolute; left: 262px; top: 50px; width: 280px;
    text-align: center; color: var(--white);
    font-weight: 600; font-size: 18.5px; line-height: 21px;
  }

  .corner-badge { position: absolute; left: 0; top: 0; width: 810px; height: 200px; }
  .event-mark { position: absolute; left: 575px; top: 96px; width: 215px; text-align: center; }
  .event-name { font-weight: 700; font-size: 30px; color: var(--navy); letter-spacing: 1px; }
  .event-tag { font-weight: 600; font-size: 8.5px; color: var(--ink); letter-spacing: 0.4px; margin-top: 2px; white-space: nowrap; }

  .headline {
    position: absolute; left: 0; top: 508px; width: 810px; text-align: center;
    font-family: "League Gothic", "Arial Narrow", sans-serif; font-weight: 400;
    color: var(--white); font-size: 134px; line-height: 118px;
    text-shadow: 0 0 14px rgba(40,25,10,0.75), 2px 3px 4px rgba(40,25,10,0.6);
  }
  .headline-line { display: block; white-space: nowrap; }
  .headline-line span { display: inline-block; transform: scaleX(0.88); }

  .tagline {
    position: absolute; left: 0; top: 774px; width: 810px; text-align: center;
    font-family: "League Gothic", "Arial Narrow", sans-serif;
    font-size: 44px; line-height: 44px; color: var(--bark); white-space: nowrap;
  }

  .details {
    position: absolute; left: 164px; top: 829px; width: 479px; height: 98px;
    background: var(--sun-orange);
    box-shadow: 8px 8px 0 var(--ink);
    text-align: center;
    font-family: "League Gothic", "Arial Narrow", sans-serif;
    font-size: 34px; line-height: 44px; color: var(--bark);
    padding-top: 5px; white-space: nowrap;
  }
  .details-text { display: inline-block; transform: scaleX(0.76); }
  .details .date { color: var(--glow); }

  .sponsors-label {
    position: absolute; left: 108px; top: 975px;
    font-family: "League Gothic", "Arial Narrow", sans-serif;
    font-size: 34px; color: var(--sun-orange);
  }
  .sponsor-row { position: absolute; left: 212px; width: 430px; display: flex; justify-content: space-between; align-items: center; }
  .sponsor-row.first { top: 955px; }
  .sponsor-row.second { top: 1005px; }
  .sponsor { font-weight: 700; font-size: 12.5px; color: var(--ink); text-align: center; line-height: 14px; }
  .sponsor.wide { max-width: 120px; }

  .footer-wave { position: absolute; left: 0; top: 1050px; width: 810px; height: 91px; }
  .footer-cta {
    position: absolute; left: 0; top: 1083px; width: 810px; text-align: center;
    color: var(--white); font-size: 25px; letter-spacing: 1px; white-space: nowrap;
  }
  .footer-cta strong { font-weight: 700; }
</style>
</head>
<body>
  <main class="flyer">
    <div class="hero-photo" role="img" aria-label="Photo of a smiling couple relaxing in camp chairs in front of a tent in an autumn forest"></div>

    <svg class="corner-badge" viewBox="0 0 810 200" aria-hidden="true">
      <path d="M560 0 H810 V190 Q700 205 640 170 Q560 120 560 0 Z" fill="#ffffff"/>
    </svg>

    <div class="hosts">
      <div class="host-name">Pinecrest Trail Council</div>
      <div class="host-name">Prairie Alliance</div>
    </div>

    <p class="intro">It’s almost time for the Rocky Mountain Region’s largest LGBT pride camping event...</p>

    <div class="event-mark">
      <div class="event-name">CAMPFEST</div>
      <div class="event-tag">MEADOWLARK’S LGBT CAMPING EVENT</div>
    </div>

    <h1 class="headline">
      <span class="headline-line"><span>DON’T MISS THIS LGBT</span></span>
      <span class="headline-line"><span>CAMPING EVENT!</span></span>
    </h1>

    <p class="tagline">Plan the highlight of your summer TODAY</p>

    <div class="details">
      <span class="details-text">Join us <span class="date">August 8th-12th</span> for 5 days of fun in a friendly, safe,<br>LGBT affirming environment for everyone, from everywhere!</span>
    </div>

    <div class="sponsors-label">sponsored by</div>
    <div class="sponsor-row first">
      <span class="sponsor">Harlow Finch</span>
      <span class="sponsor wide">Dusty’s Roadside Bar and Grill</span>
      <span class="sponsor">Vertex</span>
      <span class="sponsor">Marlo’s Uptown</span>
    </div>
    <div class="sponsor-row second">
      <span class="sponsor wide">Cedar Ridge Physical Therapy</span>
      <span class="sponsor">J’s Quickstops</span>
      <span class="sponsor">trailhub.org</span>
      <span class="sponsor">Open Field Network</span>
    </div>

    <svg class="footer-wave" viewBox="0 0 810 91" preserveAspectRatio="none" aria-hidden="true">
      <path d="M0 20 Q60 8 130 16 T260 14 T400 18 T540 12 T680 17 T810 12 V91 H0 Z" fill="#3f7a3c"/>
    </svg>
    <p class="footer-cta">More Info or Register Online <strong>www.sagebrightfest.org</strong></p>
  </main>
</body>
</html>
```